Optometric Practice needs Initial Photoshop Mockup

We need a graphic design for the homepage of a website for an optometric practice that specializes in vision therapy.

Here's the link to the project folder on Stashvale. I've included photos, example sites, content and instructions.

https://www.stashvale.example/sh/kx7rm2wq8zn41d9/BBQ_LmTyRwoPvXe3NcDrKuWjz

Please feel free to submit any questions about the design. I'll be happy to help guide you in any areas you're uncertain of.

Okay - I've updated the project to payment confirmed. Let's see some designs :) Thanks, Reg

```html
<!DOCTYPE html>
<html lang="en">
<head>
<meta charset="utf-8">
<title>BPVC – Brightpath Vision Centers of America</title>
<link href="https://fonts.googleapis.com/css2?family=Arimo:wght@400;700&family=Questrial&display=swap" rel="stylesheet">
<style>
:root{
  --red:#9c0a0f;
  --red-bright:#c0181c;
  --navy:#13125a;
  --navy-card:#23237a;
  --sky:#dfeaf3;
  --sky-deep:#b9d0e4;
  --paper:#f3f3f3;
  --ink:#222;
  --footer:#2b2b2b;
  --white:#fff;
  --fb-blue:#3b5998;
}
*{box-sizing:border-box;margin:0;padding:0}
html,body{width:800px;height:1200px;overflow:hidden}
body{position:relative;font-family:"Arimo",Arial,sans-serif;color:var(--ink);background:var(--paper)}
.abs{position:absolute}

/* header */
.top{left:0;top:0;width:800px;height:477px;background:linear-gradient(180deg,#eef4f9 0%,var(--sky) 55%,var(--sky-deep) 100%)}
.navbar{left:0;top:5px;width:800px;height:30px;background:var(--red)}
.logo-box{left:66px;top:0;width:202px;height:88px;background:var(--white);border-radius:0 0 14px 14px}
.logo-box .mark{position:absolute;left:34px;top:14px;display:flex;align-items:center;gap:7px}
.logo-box .dot{width:12px;height:12px;border-radius:50%;background:var(--navy)}
.logo-box .brand{font-family:"Questrial",sans-serif;font-size:30px;line-height:34px;color:var(--navy);letter-spacing:2px}
.logo-box .sub{position:absolute;left:14px;top:52px;font-size:7px;line-height:9px;color:#3344aa}
.nav{left:268px;top:0;height:40px;width:532px;background:var(--red);border-radius:14px 0 0 0;display:flex;align-items:center;gap:23px;padding-left:22px}
.nav a{color:var(--white);font-size:11px;text-decoration:none;white-space:nowrap}
.appt{left:403px;top:62px;width:171px;height:24px;background:#333;border-radius:3px;color:var(--white);font-size:10px;display:flex;align-items:center;gap:10px;padding-left:12px;white-space:nowrap}
.call{left:570px;top:50px;width:158px;text-align:right;white-space:nowrap}
.call .lbl{font-size:13px;color:#222}
.call .num{font-size:21px;color:var(--red)}
.hero{left:66px;top:113px;width:668px;height:313px;background:var(--white);padding:5px;box-shadow:0 1px 4px rgba(0,0,0,.25)}
.hero .photo{width:100%;height:100%;background:linear-gradient(100deg,#7a6a5c 0%,#d9d4cc 35%,#e8e4dd 55%,#a3998c 80%,#4a3f38 100%)}

/* welcome band */
.band{left:0;top:477px;width:800px;height:228px;background:var(--navy);color:var(--white)}
.welcome{left:66px;top:35px;width:206px}
.band h2{font-family:"Questrial",sans-serif;font-weight:400;font-size:20px;margin-bottom:10px;white-space:nowrap}
.welcome p{font-size:9.2px;line-height:13.4px}
.btn-more{left:191px;top:180px;width:68px;height:17px;border-radius:4px;background:var(--red-bright);color:var(--white);font-size:9px;font-weight:700;text-align:center;line-height:17px}
.video{left:297px;top:38px;width:212px;height:151px;background:#111;padding:4px}
.video .frame{height:130px;background:linear-gradient(135deg,#5a3a22,#9b6a4a 50%,#3c2a52)}
.video .play{position:absolute;left:92px;top:55px;width:28px;height:24px;background:rgba(0,0,0,.6)}
.video .bar{height:10px;margin-top:3px;border-top:1px solid #555}
.stories{left:543px;top:35px;width:200px}
.stories .card{margin-top:8px;background:var(--navy-card);border-radius:10px;padding:12px 10px 10px 8px;height:131px;position:relative}
.stories .q{position:absolute;left:6px;top:2px;font-size:28px;color:#3b3b9a;font-family:Georgia,serif}
.stories p{font-size:8.8px;line-height:13.3px;padding-left:10px}
.stories .link{display:block;margin-top:10px;padding-left:2px;font-size:8px;font-weight:700;color:var(--red-bright)}

/* services */
.services{left:72px;top:733px;width:410px}
.services h3{font-size:10px;font-weight:700;color:var(--red);margin-bottom:10px;white-space:nowrap}
.services ul{list-style:none}
.services li{font-size:8.2px;line-height:10px;padding-left:9px;position:relative;margin-bottom:10px}
.services li::before{content:"";position:absolute;left:0;top:3px;width:3px;height:3px;border-radius:50%;background:#222}
.fb{left:537px;top:727px;width:195px;height:273px;background:var(--white);border:1px solid #bbb;font-size:7px}
.fb .head{height:21px;background:var(--fb-blue);color:var(--white);display:flex;justify-content:space-between;align-items:center;padding:0 6px}
.fb .head b{font-size:12px}
.fb .page{display:flex;gap:4px;padding:5px}
.fb .thumb{width:28px;height:28px;background:#c9b9a8;flex:none}
.fb .page .nm{color:var(--fb-blue);font-weight:700;font-size:8px}
.fb .like{display:inline-block;margin-top:2px;background:var(--fb-blue);color:#fff;padding:1px 4px;font-size:7px}
.fb .feed{margin:0 5px;border-top:1px solid #ddd;border-bottom:1px solid #ddd;height:120px;overflow:hidden}
.fb .post{display:flex;gap:5px;padding:6px 0}
.fb .post .thumb{width:22px;height:22px;background:#ccc}
.fb .post b{color:var(--fb-blue)}
.fb .post p{line-height:10px;color:#333}
.fb .count{padding:4px 5px;color:#333}
.fb .faces{display:grid;grid-template-columns:repeat(6,28px);gap:3px;padding:0 5px}
.fb .faces span{height:28px;background:#b8b0a8}
.fb .plug{position:absolute;bottom:3px;left:5px;color:#555;font-size:6px}

/* footer */
.footer{left:0;top:1031px;width:800px;height:147px;background:var(--footer);color:var(--white)}
.f-brand{left:70px;top:50px;display:flex;align-items:center;gap:8px;font-family:"Questrial",sans-serif;font-size:32px;letter-spacing:2px}
.f-brand .dot{width:13px;height:13px;border-radius:50%;background:var(--white)}
.footer h4{font-weight:400;font-size:14px;line-height:16px;margin-bottom:10px;white-space:nowrap}
.social{left:263px;top:14px}
.social li{list-style:none;display:flex;align-items:center;gap:6px;font-size:9px;margin-bottom:6px;white-space:nowrap}
.social i{width:13px;height:13px;border-radius:2px;display:block}
.addr{left:412px;top:14px;font-size:8px;line-height:14.5px;white-space:nowrap}
.contact{left:602px;top:14px;width:130px}
.contact .in{background:var(--white);border-radius:3px;height:15px;width:118px;margin-bottom:7px}
.contact .in.big{height:31px}
.contact .send{width:43px;height:17px;background:var(--red);color:var(--white);font-size:9px;text-align:center;line-height:17px;margin-left:2px}
.copy{left:0;top:1178px;width:800px;height:22px;background:var(--navy);color:var(--white);font-size:8px;text-align:center;line-height:22px}
</style>
</head>
<body>
<header class="abs top">
  <div class="abs navbar"></div>
  <div class="abs logo-box">
    <div class="mark"><span class="dot"></span><span class="brand">BPVC</span></div>
    <span class="sub">Brightpath Vision<br>Centers of America</span>
  </div>
  <nav class="abs nav">
    <a href="#">Meet Us</a><a href="#">New Patients</a><a href="#">Vision &amp; Learning</a><a href="#">Head Injuries</a><a href="#">Professionals</a><a href="#">Contact Us</a>
  </nav>
  <div class="abs appt">
    <svg width="12" height="13" viewBox="0 0 12 13"><rect x="0.5" y="1.5" width="11" height="11" fill="none" stroke="#fff"/><rect x="0.5" y="1.5" width="11" height="3" fill="#fff"/><path d="M2 7h8M2 9.5h8M4 5v7M6 5v7M8 5v7" stroke="#fff" stroke-width=".6"/></svg>
    REQUEST AN APPOINTMENT
  </div>
  <div class="abs call"><div class="lbl">Call Us Now!</div><div class="num">410-555-0142</div></div>
  <div class="abs hero"><div class="photo" role="img" aria-label="Optometrist examining a patient with an eye scanning instrument"></div></div>
</header>

<section class="abs band">
  <div class="abs welcome">
    <h2>Welcome to Bpvc</h2>
    <p>There are many visual skills critical for reading and learning. Often, a vision problem is misdiagnosed as an attention problem or a learning disability due to similarity of symptoms. Anyone who is struggling with reading, has poor reading comprehension, or just isn't performing to their full potential, should consider scheduling a developmental vision evaluation.</p>
  </div>
  <div class="abs btn-more">read more...</div>
  <div class="abs video">
    <div class="frame" role="img" aria-label="Video still of a news presenter in a studio"></div>
    <div class="play"><svg width="28" height="24"><path d="M11 7l8 5-8 5z" fill="#fff"/></svg></div>
    <div class="bar"></div>
  </div>
  <div class="abs stories">
    <h2>Success Stories</h2>
    <div class="card">
      <span class="q">“</span>
      <p>simply dummy text of the printing and typesetting industry. Lorem Ipsum has been the simply dummy text of the printing and typesetting industry. Lorem Ipsum has been the &nbsp;simply dummy.</p>
      <span class="link">Vision Therapy Success Stories...</span>
    </div>
  </div>
</section>

<section class="abs services">
  <h3>The Brightpath Learning Centers of America and Dr. Daniel Marrow provide:</h3>
  <ul>
    <li>Comprehensive Eye Examinations for All Ages, including Infants and Preschoolers</li>
    <li>Vision Therapy for All Ages</li>
    <li style="margin-bottom:16px">Treatment for Learning-related Vision Problems</li>
    <li style="margin-bottom:16px">Free Monthly Seminars. Visit our Friendpage page for information about our free monthly seminars on a variety of topics, including: The Hidden Disability - Undiagnosed Vision Problems</li>
    <li style="margin-bottom:16px">Continuing Education seminars for Optometrists, Occupational Therapists and Physical Therapists. All CE offerings are free and board approved. For CE information and dates, see our success stories, blogs and videos on Binocular Vision Disorders</li>
    <li style="margin-bottom:16px">Visual Rehabilitation for Patients with Special Needs, such as Developmental Delays or Traumatic Brain Injury (TBI), including Autism, Stroke, Whiplash, CP, MS, etc.</li>
    <li style="margin-bottom:20px">Treatment for Stress-related Visual Problems, including Blurred Vision, Visual Stress from Reading and Computers, Eye Strain Headaches, and/or Vision-induced Stomachaches or Motion Sickness</li>
    <li>Sports Vision Correction and/or Improvement</li>
  </ul>
</section>

<aside class="abs fb">
  <div class="head"><b>friendpage</b><span>Find us on Friendpage</span></div>
  <div class="page">
    <div class="thumb" role="img" aria-label="Profile photo"></div>
    <div><div class="nm">BPVC: Dr. Daniel Marrow, Developmental Optometrist</div><span class="like">Like</span></div>
  </div>
  <div class="feed">
    <div class="post"><div class="thumb" role="img" aria-label="Profile photo"></div><p><b>Ned Farrow</b><br>I think all of Mexico should throw a party for my birthday this year. Does May 5th work for you?</p></div>
    <div class="post"><div class="thumb" role="img" aria-label="Profile photo"></div><p><b>Ned Farrow</b><br>Chirper wants to give you $50 in advertising credit for FREE. Such a deal! <span style="color:var(--fb-blue)">https://chirper.example/</span></p></div>
  </div>
  <div class="count">You and 14,596 others like Ned Farrow.</div>
  <div class="faces" role="img" aria-label="Grid of follower profile photos">
    <span></span><span></span><span></span><span></span><span></span><span></span><span></span><span></span><span></span><span></span>
  </div>
  <div class="plug">Friendpage social plugin</div>
</aside>

<footer class="abs footer">
  <div class="abs f-brand"><span class="dot"></span>BPVC</div>
  <div class="abs social">
    <h4>Social media</h4>
    <ul>
      <li><i style="background:#3b5998"></i>Follow us Friendpage</li>
      <li><i style="background:#3fa9d6"></i>Follow us Chirper</li>
      <li><i style="background:#2a6fa8"></i>Follow us Linkwork</li>
      <li><i style="background:#c4302b"></i>Clipstream</li>
    </ul>
  </div>
  <div class="abs addr">
    <h4>Address</h4>
    The Brightpath Learning Centers of America<br>Dr. Daniel Marrow<br>48 Harlow Ave. Suite 120, Room 6<br>Fernbrook, MD, 21299<br>Phone: 410-555-0142
  </div>
  <div class="abs contact">
    <h4>Contact information</h4>
    <div class="in"></div><div class="in"></div><div class="in big"></div>
    <div class="send">Send</div>
  </div>
</footer>
<div class="abs copy">© 2012 Bpvc, Inc. All rights reserved.</div>
</body>
</html>
```